Brightmoor Holdings Ltd - Logo and Business Card

Create a logo and business card design for our new company.

Canadian private investment company with holdings in Saskatchewan Oil and real-estate.

Target Market(s)

Investors

Industry/Entity Type

Finance

Contact Information for Business Card

Logo
Name - Dorian Pellham
Position - President
Phone - 306.418.7705
Website - www.brightmoorholdings.ca

Logo Text

Today. Tomorrow. Together. (Tag Line)

Colors

Designer to choose colors to be used in the design.

Requirements
Must have
• Logo Must Have - Type Font only
• Must be modern, professional and stand out from the crowd.
Nice to have
• Don't have any, blank slate.

```html
<!DOCTYPE html>
<html lang="en">
<head>
<meta charset="utf-8">
<title>Brightmoor Holdings Ltd – Business Card</title>
<link href="https://fonts.googleapis.com/css2?family=Lato:wght@400;700&display=swap" rel="stylesheet">
<style>
  :root {
    --page: #3a3532;
    --card: #1c1c1d;
    --card-front: #151516;
    --pattern-light: #3c3c3e;
    --pattern-dark: #141415;
    --blue: #1d87c9;
    --orange: #ee7d1a;
    --white: #f2f2f2;
    --silver: #a9a9ab;
    --rule: #cfcfcf;
  }
  * { margin: 0; padding: 0; box-sizing: border-box; }
  html, body { width: 1200px; height: 780px; overflow: hidden; }
  body {
    background: var(--page);
    font-family: "Lato", sans-serif;
    position: relative;
  }
  .card {
    position: absolute;
    top: 235px;
    width: 540px;
    height: 310px;
    border-radius: 4px;
    overflow: hidden;
    box-shadow: 0 14px 30px rgba(0,0,0,.45);
  }
  .card-front { left: 40px; background: var(--card-front); }
  .card-back { left: 620px; background: var(--card); }

  .front-pattern {
    position: absolute; inset: 0;
    background: linear-gradient(120deg, var(--pattern-dark) 0%, var(--pattern-light) 55%, var(--pattern-dark) 100%);
    opacity: .75;
  }
  .front-logo {
    position: absolute; left: 150px; top: 118px;
    display: flex; align-items: center; gap: 14px;
  }
  .logo-square { width: 22px; height: 22px; }
  .front-logo .logo-square { background: var(--silver); }
  .logo-name {
    font-weight: 700; text-transform: uppercase;
    letter-spacing: 2px; line-height: 1.05;
  }
  .front-logo .logo-name { color: var(--silver); font-size: 22px; }

  .back-logo {
    position: absolute; right: 34px; top: 58px;
    display: flex; align-items: center; gap: 12px;
  }
  .back-logo .logo-square { background: var(--blue); width: 18px; height: 18px; }
  .back-logo .logo-name { color: var(--blue); font-size: 20px; }

  .contact { position: absolute; left: 36px; top: 150px; color: var(--white); }
  .contact-name { font-size: 19px; font-weight: 700; }
  .contact-role { font-size: 13px; color: var(--orange); margin: 2px 0 8px; }
  .contact-line { font-size: 12.5px; line-height: 1.55; }
  .label { color: var(--orange); }

  .rule {
    position: absolute; left: 36px; right: 36px; top: 250px;
    height: 1px; background: var(--rule);
  }
  .website {
    position: absolute; right: 36px; top: 228px;
    font-size: 12.5px; color: var(--white);
  }
</style>
</head>
<body>
  <section class="card card-front">
    <div class="front-pattern" role="img" aria-label="Spot-gloss repeating monogram pattern across the card front"></div>
    <div class="front-logo">
      <span class="logo-square"></span>
      <span class="logo-name">Brightmoor<br>Holdings Ltd</span>
    </div>
  </section>

  <section class="card card-back">
    <div class="back-logo">
      <span class="logo-square"></span>
      <span class="logo-name">Brightmoor<br>Holdings Ltd</span>
    </div>
    <div class="contact">
      <p class="contact-name">Dorian Pellham</p>
      <p class="contact-role">President</p>
      <p class="contact-line"><span class="label">P:</span> 306.418.7705</p>
      <p class="contact-line"><span class="label">E:</span> dorianpellham@brightmoor.ca</p>
    </div>
    <p class="website"><span class="label">W:</span> www.brightmoorholdings.ca</p>
    <div class="rule"></div>
  </section>
</body>
</html>
```